Marrow Business Cards

Front of business card will have logo, name, address, & telephone number. Back of card will have a list of services provided - Roads, Substation Pads, Temporary Pads, Site Pads, Land Leveling, Powerline Row Cleaning, Land Clearing, Gates, Fencing, Construction Entrances, Excavation, Trenching, Underground Utilities, Directional Boring, Pile Driving. We are a construction company that uses heavy equipment like bulldozers, motor graders/blades, dump trucks, backhoes, hydro axes, & skid loaders. We build roads, pads, & install electric utility lines & waterlines underground. This logo is new. The word "Construction" can be smaller as uploaded 2 example edited logos. We will be using this card design for many employees.
Target Market(s)
Industrial Electric Powerline, Wind Turbine, Solar Panel, & Water Utility companies.
Contact Information for Business Card
Name/Position - Dorian Quale - Owner
Address: 4837 FM 582
Merkel, TX 79418
Phone number - (325) 418-2906

```html
<!DOCTYPE html>
<html lang="en">
<head>
<meta charset="utf-8">
<title>Marrow Construction Business Cards</title>
<link href="https://fonts.googleapis.com/css2?family=Montserrat:wght@500;700;800&display=swap" rel="stylesheet">
<style>
  :root {
    --gold: #e2b02a;
    --gold-deep: #d9a522;
    --maroon: #3a1117;
    --red: #c4262c;
    --paper: #ffffff;
  }
  * { margin: 0; padding: 0; box-sizing: border-box; }
  html, body { width: 1000px; height: 1200px; overflow: hidden; background: var(--paper); }
  body { position: relative; font-family: 'Montserrat', Arial, sans-serif; }

  .card {
    position: absolute;
    top: 113px;
    width: 411px;
    height: 235px;
    overflow: hidden;
    background: radial-gradient(circle at 30% 40%, var(--gold) 0%, var(--gold-deep) 100%);
  }
  .card-front { left: 65px; }
  .card-back { left: 521px; }
  .card svg.shapes { position: absolute; inset: 0; }

  .brand {
    position: absolute;
    left: 34px;
    top: 34px;
    width: 170px;
    text-align: center;
    color: var(--maroon);
    font-weight: 800;
    line-height: 1;
  }
  .brand-name { display: block; font-size: 26px; letter-spacing: 1px; }
  .brand-sub { display: block; font-size: 15px; letter-spacing: 1px; margin-top: 6px; }
  .license {
    position: absolute;
    left: 34px;
    top: 96px;
    width: 170px;
    text-align: center;
    color: var(--maroon);
    font-size: 7px;
    font-weight: 700;
    line-height: 1.1;
  }

  .contact {
    position: absolute;
    right: 22px;
    top: 88px;
    text-align: right;
    color: var(--maroon);
    font-weight: 700;
  }
  .contact-name { font-size: 14px; font-weight: 800; letter-spacing: 0.3px; }
  .contact-title { font-size: 11px; color: var(--red); font-style: italic; font-weight: 700; margin-top: 2px; }
  .contact-email { font-size: 11.5px; font-weight: 500; margin-top: 14px; }
  .contact-address { font-size: 11.5px; line-height: 1.35; margin-top: 16px; }
  .contact-phone { font-size: 12px; margin-top: 16px; }

  .website {
    position: absolute;
    left: 10px;
    top: 11px;
    color: var(--maroon);
    font-size: 16px;
    font-weight: 800;
  }
  .services {
    position: absolute;
    left: 14px;
    top: 48px;
    list-style: none;
    color: var(--gold);
    font-size: 16.5px;
    font-weight: 800;
    line-height: 19.8px;
    letter-spacing: 0.1px;
  }
  .services .sep { color: var(--red); }
</style>
</head>
<body>

  <section class="card card-front" aria-label="Business card front">
    <svg class="shapes" width="411" height="235" viewBox="0 0 411 235" aria-hidden="true">
      <polygon points="0,100 170,235 97,235 0,160" fill="var(--maroon)"/>
    </svg>
    <div class="brand">
      <span class="brand-name">MARROW</span>
      <span class="brand-sub">CONSTRUCTION</span>
    </div>
    <div class="license">CONTRACTOR LICENSE<br># 1234567</div>
    <div class="contact">
      <p class="contact-name">DORIAN QUALE</p>
      <p class="contact-title">OWNER</p>
      <p class="contact-email">dorian@marrowconstruction.com</p>
      <p class="contact-address">4837 FM 582<br>MERKEL, TX 79418</p>
      <p class="contact-phone">(325) 418-2906</p>
    </div>
  </section>

  <section class="card card-back" aria-label="Business card back">
    <svg class="shapes" width="411" height="235" viewBox="0 0 411 235" aria-hidden="true">
      <polygon points="0,40 330,40 411,75 411,235 0,235" fill="var(--maroon)"/>
    </svg>
    <p class="website">www.marrowconstruction.com</p>
    <ul class="services">
      <li>ROADS<span class="sep">/</span>SUBSTATION PADS<span class="sep">/</span></li>
      <li>TEMPORARY PADS<span class="sep">/</span>SITE PADS<span class="sep">/</span></li>
      <li>LAND LEVELING<span class="sep">/</span></li>
      <li>POWERLINE ROW CLEANING<span class="sep">/</span></li>
      <li>LAND CLEARING<span class="sep">/</span>GATES<span class="sep">/</span>FENCING<span class="sep">/</span></li>
      <li>CONSTRUCTION ENTRANCES<span class="sep">/</span></li>
      <li>EXCAVATION<span class="sep">/</span>TRENCHING<span class="sep">/</span></li>
      <li>UNDERGROUND UTILITIES<span class="sep">/</span></li>
      <li>DIRECTIONAL BORING<span class="sep">/</span>PILE DRIVING<span class="sep">/</span></li>
    </ul>
  </section>

</body>
</html>
```